Corrindale Planners, LLC Stationary

Corrindale Planners, LLC is a new financial planning and consulting company. We are looking for designs on business cards, letterhead, envelopes, and anything else that would be useful. Our preference for business card design is two sided. We are looking for a professional and clean look with incorporating the logo and patriotic feel. Thank you to all who participate and good luck!

```html
<!DOCTYPE html>
<html lang="en">
<head>
<meta charset="utf-8">
<title>Corrindale Planners, LLC — Stationery</title>
<link href="https://fonts.googleapis.com/css2?family=Questrial&display=swap" rel="stylesheet">
<style>
  :root{
    --backdrop:#cfcfcf;
    --paper:#f1f1f1;
    --navy:#123d69;
    --red:#b71f27;
    --ink:#2b2b2b;
    --soft-white:#e9eef4;
  }
  *{box-sizing:border-box;margin:0;padding:0}
  html,body{width:1200px;height:1041px;overflow:hidden}
  body{background:var(--backdrop);font-family:"Questrial",sans-serif;color:var(--ink);position:relative}
  .piece{position:absolute;background:var(--paper);overflow:hidden}

  .brand{color:var(--navy);text-transform:uppercase;letter-spacing:.04em;line-height:1.05;display:flex;align-items:center;gap:6px}
  .brand-dot{display:inline-block;border-radius:50%;background:var(--red);flex:none}
  .tagline{color:var(--red);text-transform:uppercase;letter-spacing:.14em}

  /* Folder */
  .folder{left:166px;top:76px;width:418px;height:541px}
  .folder-spine{position:absolute;left:25px;top:0;bottom:0;width:1px;background:rgba(0,0,0,.12)}
  .folder-head{height:222px;display:flex;flex-direction:column;align-items:center;justify-content:center;padding-left:20px}
  .folder-head .brand{font-size:17px}
  .folder-head .brand-dot{width:14px;height:14px}
  .folder-head .tagline{font-size:6.5px;margin-top:8px}
  .folder-body{height:254px;background:var(--navy)}
  .folder-foot{height:65px;background:var(--red);color:#f3d6d6;font-size:8px;display:flex;align-items:center;justify-content:center;padding-left:20px;letter-spacing:.03em}

  /* Letterhead */
  .letterhead{left:615px;top:95px;width:403px;height:522px}
  .letterhead .brand-block{position:absolute;left:37px;top:38px}
  .letterhead .brand{font-size:11px}
  .letterhead .brand-dot{width:9px;height:9px}
  .letterhead .tagline{font-size:4.5px;margin-top:5px}
  .letter-body{position:absolute;left:37px;top:156px;width:330px;font-size:5.4px;line-height:1.3;text-align:justify}
  .letter-body p{margin-bottom:6px}
  .letter-body .greeting{font-weight:bold}
  .sign-off{display:flex;align-items:flex-start;gap:8px;margin-top:4px}
  .sign-off strong{display:block}
  .signature{width:80px;height:28px;background:#e4e7f0}
  .letter-footer{position:absolute;left:0;right:0;bottom:6px;height:18px;background:var(--navy);color:#dfe6ee;font-size:5px;display:flex;align-items:center;padding:0 37px;gap:22px}
  .letter-footer .contacts{display:flex;gap:10px;margin-left:auto}
  .letter-footer .contacts span{display:flex;align-items:center;gap:3px}
  .letter-footer .contacts i{width:5px;height:5px;background:var(--red);display:inline-block}
  .red-rule{position:absolute;left:0;right:0;bottom:0;height:6px;background:var(--red)}

  /* Envelope front */
  .env-front{left:132px;top:645px;width:451px;height:195px}
  .env-front .brand-block{position:absolute;left:20px;top:33px}
  .env-front .brand{font-size:11px}
  .env-front .brand-dot{width:9px;height:9px}
  .env-front .tagline{font-size:4.5px;margin-top:5px}
  .env-front-band{position:absolute;left:0;right:0;bottom:6px;height:14px;background:var(--navy);color:#dfe6ee;font-size:5px;display:flex;align-items:center;padding-left:35px}

  /* Envelope back */
  .env-back{left:615px;top:645px;width:451px;height:195px}
  .env-flap{position:absolute;left:0;top:0;width:451px;height:64px}
  .env-back .url{position:absolute;left:0;right:0;top:170px;text-align:center;font-size:5.5px;color:#555}

  /* Business cards */
  .card-front{left:416px;top:870px;width:167px;height:96px;background:var(--navy)}
  .card-front .brand{position:absolute;left:0;right:0;top:38px;justify-content:center;color:#fff;font-size:7.5px;flex-direction:row}
  .card-front .brand-dot{width:6px;height:6px}
  .card-front .tagline{position:absolute;left:0;right:0;top:52px;text-align:center;font-size:3.4px;color:#e8a3a6}
  .card-red{position:absolute;left:0;right:0;bottom:0;height:8px;background:var(--red)}

  .card-back{left:615px;top:870px;width:167px;height:96px}
  .card-back .person{position:absolute;left:10px;top:25px;font-size:5px;color:var(--navy)}
  .card-back .person strong{display:block;letter-spacing:.05em}
  .card-back .person span{color:#666;font-size:4.2px}
  .card-back .brand-block{position:absolute;right:12px;top:20px;text-align:center}
  .card-back .brand{font-size:7px}
  .card-back .brand-dot{width:5px;height:5px}
  .card-back .tagline{font-size:2.8px;margin-top:3px}
  .card-back-band{position:absolute;left:0;right:0;top:52px;height:36px;background:var(--navy);color:#dfe6ee;font-size:3.8px;line-height:1.45;display:flex;justify-content:space-between;padding:6px 9px 0 17px}
  .card-back-band .addr{text-align:right}
  .card-notch{position:absolute;left:10px;top:51px;width:0;height:0;border-left:3px solid transparent;border-right:3px solid transparent;border-top:4px solid var(--paper)}
</style>
</head>
<body>

<section class="piece folder" aria-label="Presentation folder">
  <div class="folder-spine"></div>
  <div class="folder-head">
    <div class="brand"><span class="brand-dot"></span>Corrindale Planners, LLC</div>
    <div class="tagline">Financial Planning and Consulting</div>
  </div>
  <div class="folder-body"></div>
  <div class="folder-foot">www.corrindaleplan.com</div>
</section>

<section class="piece letterhead" aria-label="Letterhead">
  <div class="brand-block">
    <div class="brand"><span class="brand-dot"></span>Corrindale Planners, LLC</div>
    <div class="tagline">Financial Planning and Consulting</div>
  </div>
  <div class="letter-body">
    <p class="greeting">Dear sir,</p>
    <p>Communication is a very integral part of living creatures, animals and humans. Communication may be verbal or written. Written communication however is only applicable to human beings. Can you even imagine a world without communication? Verbal communication can be through telephones, webcams or in person. Written communication is through letters, emails and mobile phone messages.</p>
    <p>In today's world of great inventions and technology, letters have somehow become redundant. It is the time for text messages or chats. But they still can communicate a lot more than all other modes of communication. Organizations and various government departments still bank on letters as a strong medium of communication. There is no comparison in costs of sending letters as compared to costs of mobile phone messages though – letters are far cheaper. Letters now commonly known as "hard copy documents" are considered more relevant and important than email copies of text messages as proof or evidence of some sort.</p>
    <p>Letters speak volumes about a person or an organization that writes it. So one must take utmost care ensuring that the language used in any letter is appropriate for the occasion for which it is being written. Since a letter is also a written proof or document, if there are certain things that should not form a part of it, then that too should be carefully handled.</p>
    <p>Writing a good letter is an art. But if for some reason someone is unable to write that perfect letter, these different types of letters provide a base for you to build on. Sample letters have been given for everyone to understand what all information needs to form a part of the letter type and then it can be customized.</p>
    <div class="sign-off">
      <div>Yours Sincerely,<strong>Lena Marsh</strong></div>
      <div class="signature" role="img" aria-label="Handwritten signature"></div>
    </div>
  </div>
  <div class="letter-footer">
    <span>418 N. Harwell Ave, Suite C, Larkspur CA 91508</span>
    <div class="contacts">
      <span><i></i>555.210.4830</span>
      <span><i></i>info@corrindaleplan.com</span>
      <span><i></i>www.corrindaleplan.com</span>
    </div>
  </div>
  <div class="red-rule"></div>
</section>

<section class="piece env-front" aria-label="Envelope front">
  <div class="brand-block">
    <div class="brand"><span class="brand-dot"></span>Corrindale Planners, LLC</div>
    <div class="tagline">Financial Planning and Consulting</div>
  </div>
  <div class="env-front-band">418 N. Harwell Ave, Suite C, Larkspur CA 91508</div>
  <div class="red-rule"></div>
</section>

<section class="piece env-back" aria-label="Envelope back">
  <svg class="env-flap" viewBox="0 0 451 64" aria-hidden="true">
    <path d="M0 0H451L436 60Q435 64 430 64H21Q16 64 15 60Z" fill="#123d69"/>
    <circle cx="225.5" cy="33" r="6" fill="#b71f27"/>
  </svg>
  <div class="url">www.corrindaleplan.com</div>
</section>

<section class="piece card-front" aria-label="Business card front">
  <div class="brand"><span class="brand-dot"></span>Corrindale Planners, LLC</div>
  <div class="tagline">Financial Planning and Consulting</div>
  <div class="card-red"></div>
</section>

<section class="piece card-back" aria-label="Business card back">
  <div class="person"><strong>OWEN TELLER</strong><span>General Manager</span></div>
  <div class="brand-block">
    <div class="brand"><span class="brand-dot"></span>Corrindale<br>Planners, LLC</div>
    <div class="tagline">Financial Planning and Consulting</div>
  </div>
  <div class="card-back-band">
    <div>555.210.4830<br>555.210.4840<br>info@corrindaleplan.com<br>www.corrindaleplan.com</div>
    <div class="addr"><br>418 N. Harwell Ave<br>Suite C<br>Larkspur CA 91508</div>
  </div>
  <div class="card-notch"></div>
  <div class="card-red"></div>
</section>

</body>
</html>
```